Brightleaf Wellness Website Design

About The Client:
Brightleaf Wellness is a sugar-free foods chain store providing services to Diabetics. They focus on the China domestic market. They describe themselves as being the 3rd space for Diabetics, the space between hospital and the home that help improve the quality of life for people wit Diabetes (see attached infographics).

They regularly hold education and advice events throughout the China. Brightleaf Wellness distribute a wide product range of food that is suitable for diabetic people. Brightleaf Wellness operate as a Franchise, providing business development services and Industry knowledge. They are actively seeking business partnerships at present.

The Brief:
Design a Home page and secondary information page(PSD only no code) that communicates our company services and company philosophy(3rd Space).
The final design should communicate 'Health, Social Responsibility and Professionalism'.
Colour scheme should orientate around Blue and White, see attached logo.

Websites we like:

http://link.venomira.com/home/

https://www.paxtunel.com/

http://dev.zorvik.com/
Updates

Hello all, the client has advised us that he want to display the professional advice service available for diabetic people more so than a food distributor. The client is also hoping to use his website as a marketing platform to attract affiliates and build partnerships as part of Brightleaf Wellness's business expansion strategy.

So can you make the page more corporate, reliable and professional. Use images of experts/doctors interacting with patients and also training/knowledge transfer images.

Thanks

Hello all, could you include stock images of both Chinese and Caucasians

Yeaahhh, Infographics and photos have been uploaded. Feel free to use them in your designs and also as references.

Target Market(s)

The target market is Chinese B2B in the Diabetics industry and Entrepreneurs looking to cooperate with Brightleaf Wellness.

Industry/Entity Type

Education

Requirements
Must have
• menu navigation with 7-8 sections,
a full screen background image,
Social Media icons,
Logo in top left,
Site search.
Nice to have
• The website must be clear and easy to use, less complicated.

See attached files of some Brightleaf Wellness infographics. Feel free to include elements of these into the design.
Should not have
• Should not use stock images of people from any other country, the client wants stock images of Chinese people only. Avoid photos showing obesity.

```html
<!DOCTYPE html>
<html lang="en">
<head>
<meta charset="utf-8">
<title>Brightleaf Wellness – Home</title>
<link href="https://fonts.googleapis.com/css2?family=Roboto+Condensed:wght@400;700&display=swap" rel="stylesheet">
<style>
:root{
  --blue:#1a9fe0;
  --blue-dark:#0b7fc4;
  --blue-title:#1478b8;
  --red:#e03038;
  --red-dark:#c41f28;
  --text:#444;
  --muted:#666;
  --line:#d4d4d4;
  --panel:#f1f2f2;
  --page:#f7f7f7;
  --white:#fff;
}
*{box-sizing:border-box;margin:0;padding:0}
html,body{width:1200px;height:1142px;overflow:hidden;background:var(--white);font-family:"Roboto Condensed",Arial,sans-serif;color:var(--text)}
.canvas{position:relative;width:1200px;height:1142px}
.abs{position:absolute}

.site-header{position:absolute;left:0;top:0;width:1200px;height:106px;background:var(--white);border-top:2px solid #eee;border-bottom:1px solid #ddd}
.brand{position:absolute;left:181px;top:38px;display:flex;align-items:center;gap:10px;font-size:24px;font-weight:700;color:var(--blue)}
.brand-mark{width:26px;height:26px;border-radius:50%;background:var(--blue)}
.social{position:absolute;left:802px;top:27px;display:flex;gap:10px}
.social span{width:15px;height:15px;border-radius:50%;background:var(--blue)}
.search{position:absolute;left:864px;top:19px;width:181px;height:31px;border:1px solid #ccc;box-shadow:inset 0 0 0 2px #f3f3f3;font-size:14px;color:#777;padding:7px 9px}
.search svg{position:absolute;right:8px;top:6px}
.nav{position:absolute;left:445px;top:70px;display:flex;list-style:none;font-size:16px;color:#555}
.nav li{height:36px;padding:2px 14px 0}
.nav li.active{color:var(--blue);border-bottom:4px solid var(--blue)}

.hero{position:absolute;left:0;top:106px;width:1200px;height:381px;background:linear-gradient(90deg,#2c8f8f 0%,#b8752e 18%,#d9862a 40%,#c96a2b 55%,#c7b8a6 66%,#d68a30 80%,#2a8e90 100%)}
.hero-band{position:absolute;left:0;top:243px;width:1200px;height:97px;background:rgba(20,40,45,.78)}
.hero-text{position:absolute;left:181px;top:265px;font-size:23px;line-height:27px;color:var(--white)}
.hero-text strong{color:#33b4ee}
.dots{position:absolute;left:567px;top:351px;display:flex;gap:4px}
.dots span{width:17px;height:17px;border-radius:50%;background:#6f6f6f;border:1px solid #555}
.dots span.on{background:var(--blue);border-color:#0d7fc0}

.content{position:absolute;left:0;top:487px;width:1200px;height:555px;background:var(--page);border-bottom:1px solid #ddd}
.card{position:absolute;top:22px;width:290px;height:247px;background:var(--panel);border:1px solid #cfcfcf;text-align:center}
.card h3{margin-top:15px;font-size:16px;color:var(--blue-title)}
.card .photo{margin:9px auto 0;width:254px;height:101px;border:1px solid #c9c9c9;background:var(--white);padding:4px}
.card .photo div{width:100%;height:100%}
.card p{margin:9px 12px 0;font-size:12.5px;line-height:14.5px;color:var(--muted)}
.btn{display:inline-block;background:linear-gradient(#40b8f0,#1590d6);border:1px solid #0e7fc0;border-radius:2px;color:var(--white);font-weight:700;font-size:12px;text-align:center}
.card .btn{margin-top:11px;width:115px;height:29px;line-height:27px}

.section-title{position:absolute;top:299px;font-size:16px;color:#555;padding-bottom:8px;border-bottom:1px dashed #bbb}
.section-title strong{color:var(--blue-title)}
.welcome-copy{position:absolute;left:148px;top:342px;width:594px;font-size:12.5px;line-height:14.7px;color:var(--muted)}
.welcome-copy p+p{margin-top:15px}
.big-btn{position:absolute;top:478px;width:192px;height:44px;border-radius:3px;color:var(--white);font-weight:700;font-size:15px;line-height:44px;text-align:center;background:linear-gradient(#58c3f2 0 45%,#1d9ae0 46%,#0d86cc);border:1px solid #0d79b8}
.big-btn.red{background:linear-gradient(#f06a70 0 45%,#e03038 46%,var(--red-dark));border-color:#b01c24}

.field{position:absolute;left:755px;width:292px;background:var(--white);border:1px solid #ccc;font-size:12.5px;color:#555;padding:7px 5px}
.submit{position:absolute;left:840px;top:485px;width:116px;height:29px;line-height:27px}

.footer{position:absolute;left:0;top:1076px;width:1200px;text-align:center;font-size:11.5px;line-height:16px;color:#666}
</style>
</head>
<body>
<div class="canvas">
  <header class="site-header">
    <div class="brand"><span class="brand-mark"></span>Brightleaf Wellness</div>
    <div class="social"><span></span><span></span></div>
    <div class="search">Search
      <svg width="18" height="18" viewBox="0 0 18 18"><circle cx="7" cy="7" r="5.5" fill="none" stroke="#8a9aa6" stroke-width="2"/><line x1="11" y1="11" x2="16.5" y2="16.5" stroke="#8a9aa6" stroke-width="2.5" stroke-linecap="round"/></svg>
    </div>
    <ul class="nav">
      <li class="active">Home</li><li>About Us</li><li>Services</li><li>Food Store</li><li>Our Philosophy</li><li>Events</li><li>Contact Us</li>
    </ul>
  </header>

  <section class="hero" role="img" aria-label="Supermarket produce aisle with a smiling staff member holding a blue heart balloon">
    <div class="hero-band"></div>
    <div class="hero-text">We just not only sale food but<br>also made our <strong>Social Responsibilities</strong>.</div>
    <div class="dots"><span class="on"></span><span></span><span></span></div>
  </section>

  <main class="content">
    <div class="card" style="left:147px">
      <h3>Our Philosophy</h3>
      <div class="photo"><div role="img" aria-label="Woman stretching in a bright room" style="background:linear-gradient(#e4e6e8,#c9cdd0)"></div></div>
      <p>Lorem ipsum dolor sit amet, consectetur adipisicing elit, sed do eiusmod tempor incididunt ut labore et dolore magna aliqua.</p>
      <span class="btn">Know More</span>
    </div>
    <div class="card" style="left:452px">
      <h3>Our Services</h3>
      <div class="photo"><div role="img" aria-label="Store assistant in an apron at a shop counter" style="background:linear-gradient(90deg,#c7ccd2,#e9ebee 50%,#b9bec4)"></div></div>
      <p>Lorem ipsum dolor sit amet, consectetur adipisicing elit, sed do eiusmod tempor incididunt ut labore et dolore magna aliqua.</p>
      <span class="btn">Know More</span>
    </div>
    <div class="card" style="left:756px">
      <h3>Our Events</h3>
      <div class="photo"><div role="img" aria-label="People talking together at a cafe event" style="background:linear-gradient(90deg,#6b4a38,#a27a60 50%,#5a4236)"></div></div>
      <p>Lorem ipsum dolor sit amet, consectetur adipisicing elit, sed do eiusmod tempor incididunt ut labore et dolore magna aliqua.</p>
      <span class="btn">Know More</span>
    </div>

    <h2 class="section-title" style="left:148px;width:594px"><strong>Welcome</strong> to our site</h2>
    <div class="welcome-copy">
      <p>Lorem ipsum dolor sit amet, consectetur adipisicing elit, sed do eiusmod tempor incididunt ut labore et dolore magna aliqua. Lorem ipsum dolor sit amet, consectetur adipisicing elit, sed do eiusmod tempor incididunt ut labore et dolore magna aliqua. Lorem ipsum dolor sit amet, consectetur adipisicing elit, sed do eiusmod tempor incididunt ut labore et dolore magna aliqua.</p>
      <p>Lorem ipsum dolor sit amet, consectetur adipisicing elit, sed do eiusmod tempor incididunt ut labore et dolore magna aliqua. Lorem ipsum dolor sit amet, consectetur adipisicing elit, sed do eiusmod tempor incididunt ut labore et dolore magna aliqua.</p>
    </div>
    <div class="big-btn" style="left:148px">OUR TRAINING</div>
    <div class="big-btn red" style="left:350px">PERTNERSHIP</div>
    <div class="big-btn" style="left:553px">FOR DIABETICS</div>

    <h2 class="section-title" style="left:755px;width:292px"><strong>Query Us</strong> to help you</h2>
    <div class="field" style="top:341px;height:29px">Email</div>
    <div class="field" style="top:379px;height:91px">Query</div>
    <span class="btn submit">Submit</span>
  </main>

  <footer class="footer">Copyright@2013. All rights are reserved.<br>Terms &amp; Privacy Policy</footer>
</div>
</body>
</html>
```